harbor mental health stationary

Please help turn this logo into a total image for my business.
Stationary need to be able to be individualized for each mental health practitioners

Some generic info about services
Clinical Psychology - Consultant Psychiatry - Locum Services - Medico-legal - Architectural Adviser Clinical and Medical Facilities

Target Market(s)

Letter head for doctors, courts, patients.

Industry/Entity Type

Mental Health

Requirements
Must have
• area where practitioners details can be listed and logo on page
Nice to have
• embossed section

```html
<!DOCTYPE html>
<html lang="en">
<head>
<meta charset="utf-8">
<title>Harbor Mental Health – Letterhead</title>
<link href="https://fonts.googleapis.com/css2?family=Montserrat:wght@300;400;600&family=Tinos:ital,wght@0,400;0,700;1,700&display=swap" rel="stylesheet">
<style>
  :root {
    --backdrop: #e6e6e6;
    --paper: #ffffff;
    --brand: #1f3b5c;
    --ink: #1a1a1a;
    --muted: #555b63;
    --rule: #8a8f96;
    --accent: #2f6f9a;
  }
  * { margin: 0; padding: 0; box-sizing: border-box; }
  html, body { width: 1200px; height: 909px; overflow: hidden; }
  body { background: var(--backdrop); font-family: "Montserrat", sans-serif; color: var(--ink); position: relative; }

  .letterhead {
    position: absolute; left: 296px; top: 24px; width: 608px; height: 860px;
    background: var(--paper); box-shadow: 0 2px 10px rgba(0,0,0,.12);
  }

  .brand { position: absolute; left: 42px; top: 52px; display: flex; align-items: center; gap: 9px; }
  .brand-square { width: 22px; height: 22px; background: var(--brand); }
  .brand-name { font-family: "Montserrat", sans-serif; font-weight: 600; font-size: 17px; letter-spacing: 1.2px; color: var(--brand); line-height: 1; }

  .contact { position: absolute; left: 352px; top: 44px; font-size: 7px; line-height: 12px; color: var(--muted); }
  .contact .row { display: flex; gap: 16px; }
  .contact .icon { color: var(--accent); font-weight: 600; margin-right: 4px; }
  .contact b { color: var(--ink); font-weight: 600; }

  .practitioner { position: absolute; left: 42px; right: 42px; top: 92px; border-top: 0.75px solid var(--rule); padding-top: 5px; font-size: 6.5px; color: var(--muted); }
  .practitioner .name { color: var(--ink); font-weight: 600; }
  .practitioner .member { text-align: right; margin-top: 2px; }

  .letter { position: absolute; left: 60px; right: 60px; top: 150px; font-family: "Tinos", serif; font-weight: 700; font-size: 11px; line-height: 13.2px; color: var(--ink); text-align: justify; }
  .letter p { margin-bottom: 13px; }
  .letter em { font-style: italic; }
  .closing { margin-top: 46px; margin-left: 212px; }
  .signature { display: block; width: 90px; height: 34px; margin: 6px 0 2px; background: linear-gradient(90deg, #d9d9d9, #bfbfbf); border-radius: 3px; }
  .signer { font-size: 9.5px; }

  .services { position: absolute; right: 42px; bottom: 40px; text-align: right; font-family: "Montserrat", sans-serif; font-weight: 300; font-size: 9.5px; line-height: 14px; color: var(--muted); }
</style>
</head>
<body>
  <main class="letterhead">
    <header>
      <div class="brand">
        <span class="brand-square"></span>
        <span class="brand-name">HARBOR MENTAL HEALTH</span>
      </div>
      <address class="contact">
        <div>24 Marlow Court, BAYSIDE 6031</div>
        <div class="row"><span><span class="icon">T</span>(08) 9000 4182</span><span><span class="icon">M</span>0400 123 987</span></div>
        <div><span class="icon">E</span>mhale@hmh.example</div>
        <div><b>ABN:</b> 00 000 000 000 <b>ACN:</b> 000000000</div>
      </address>
      <div class="practitioner">
        <div><span class="name">Megan Hale M.</span> Psych (Clinical), M. Genetic Couns., B.A. (Psych) Reg. no: PSY0000000 Provider no: 0000000K</div>
        <div class="member">Member of the National Psychological Society</div>
      </div>
    </header>

    <section class="letter">
      <p>Gentlemen,</p>
      <p>Enclosed I have the honor to send you an article which I should be pleased if you would accept for the “Meridian Review”. I am <em>desperately</em> pushed for money; and in the event of Mr. O’Connell’s liking the “Landscape-Garden”, I would take it as an especial favor if you would mail me the amount due for it, so as to reach me here by the 21st, on which day I shall need it. Can you possibly oblige me in this? If you accept the paper I presume you will allow me your usual sum, whatever that is for similar contributions—but I set no price—leaving all to your own liberality. The piece will make 8 of your pages and rather more.</p>
      <p>Will you be kind enough to put the best possible interpretation upon my behavior while in Port Ellis? You must have conceived a <em>queer</em> idea of me—but the simple truth is that Whitmore would insist upon <em>the juleps</em>, and I knew not what I was either doing or saying. The Review of Dorsey which I offered you was deficient in a 1/2 page of commencement, which I had written to supersede the old beginning, and which gave the article the character of a general and retrospective review. No wonder you did not take it—I would have been very much mortified if you had. I hope to see you at some future time, under better auspices.</p>
      <div class="closing">
        <div>In the meantime I remain</div>
        <div>Yours very truly,</div>
        <span class="signature" role="img" aria-label="Handwritten signature"></span>
        <div class="signer">Elias Alden Pike</div>
      </div>
    </section>

    <footer class="services">
      <div>Clinical Psychology - Consultant Psychiatry - Locum Services - Medico-legal</div>
      <div>Architectural Adviser Clinical and Medical Facilities</div>
    </footer>
  </main>
</body>
</html>
```